CordaVex Packaging, for retail brand of graduation tassels

Retail packaging for graduation tassels. Leave space for a UPC on the back bottom of the template. Design must bleed over edges for printing. Use the attached logo in the packaging. The photo is an example of the packaging, but does not match the template. Please use the shape and dimensions of the template. Please provide all standard file formats. The packaging is not specific to a SKU, it is general.
You can change the color of the logo and add the "TM"

Font styles to use
Other font styles liked:
• See logo

Colors

Designer to choose colors to be used in the design.

Requirements
Must have
• Brand logo, color bleeds on the template
• Include any or all of the following information, either on the back or used as call outs on the packaging.
• "Our tassels are made from the highest quality of polyester available, resulting in accurate and consistent school colors. Each tassel has 50-60 braided yarns. The signets are made from Zinc alloy or solid brass (depending on color)"
Nice to have
• gets the attention of consumers
Should not have
• nothing specific to a SKU

```html
<!DOCTYPE html>
<html lang="en">
<head>
<meta charset="utf-8">
<title>CordaVex Tassel Box Template</title>
<link href="https://fonts.googleapis.com/css2?family=Montserrat:wght@400;600;700&display=swap" rel="stylesheet">
<style>
  :root {
    --page: #ffffff;
    --board: #050505;
    --cut: #1c1f5e;
    --fold: #2a2f80;
    --gold: #e2ab2b;
    --gold-light: #ffe07a;
    --gold-dark: #b57a12;
    --label: #ffffff;
    --ink: #1a1a1a;
    --upc: #8a8a8a;
  }
  html, body {
    margin: 0;
    width: 1200px;
    height: 1200px;
    overflow: hidden;
    background: var(--page);
  }
  .canvas {
    width: 1200px;
    height: 1200px;
    display: flex;
    align-items: center;
    justify-content: center;
  }
  .dieline { width: 446px; height: 1120px; display: block; }
  .board { fill: var(--board); stroke: var(--cut); stroke-width: 1.2; stroke-linejoin: round; }
  .fold { stroke: var(--fold); stroke-width: 0.8; fill: none; }
  .hang-hole { fill: none; stroke: var(--fold); stroke-width: 1; }
  .window { fill: #ffffff; stroke: url(#goldEdge); stroke-width: 3.5; }
  .brand-name {
    font-family: "Montserrat", sans-serif;
    font-weight: 700;
    fill: var(--gold);
    text-anchor: middle;
    dominant-baseline: middle;
  }
  .info-label { fill: var(--label); }
  .info-text {
    font-family: "Montserrat", sans-serif;
    font-weight: 400;
    font-size: 6.2px;
    fill: var(--ink);
  }
  .info-bullet { fill: var(--ink); }
  .upc-note {
    font-family: "Montserrat", sans-serif;
    font-weight: 600;
    font-size: 15px;
    fill: var(--upc);
    text-anchor: middle;
  }
</style>
</head>
<body>
<main class="canvas">
  <svg class="dieline" viewBox="60 100 400 1005" xmlns="http://www.w3.org/2000/svg" aria-label="CordaVex tassel box dieline">
    <defs>
      <linearGradient id="goldEdge" x1="0" y1="0" x2="1" y2="1">
        <stop offset="0" stop-color="var(--gold-light)"/>
        <stop offset="0.5" stop-color="var(--gold)"/>
        <stop offset="1" stop-color="var(--gold-dark)"/>
      </linearGradient>
    </defs>

    <!-- glue flap -->
    <path class="board" d="M120 262 L76 272 L73 1055 L120 1062 Z"/>

    <!-- back panel with hang tab -->
    <path class="board" d="M110 262 L110 140 L124 115 L223 115 L237 140 L237 262 Z"/>
    <circle class="hang-hole" cx="175" cy="185" r="11"/>
    <circle class="hang-hole" cx="175" cy="225" r="11"/>
    <path class="board" d="M118 1040 L130 1090 L221 1090 L233 1040 Z"/>

    <!-- side and front top flaps -->
    <path class="board" d="M233 262 L240 222 L272 222 L278 262 Z"/>
    <path class="board" d="M278 262 L278 215 L272 215 L272 182 Q272 172 282 172 L388 172 Q398 172 398 182 L398 215 L392 215 L392 262 Z"/>
    <path class="board" d="M392 262 L398 222 L434 222 L445 262 Z"/>

    <!-- bottom flaps -->
    <path class="board" d="M233 1040 L238 1078 L273 1078 L278 1040 Z"/>
    <path class="board" d="M278 1040 L284 1074 L310 1074 L314 1090 L356 1090 L360 1074 L386 1074 L392 1040 Z"/>
    <path class="board" d="M392 1040 L399 1088 L438 1088 L445 1040 Z"/>

    <!-- main body -->
    <rect class="board" x="118" y="262" width="327" height="778"/>

    <!-- fold lines -->
    <line class="fold" x1="120" y1="262" x2="120" y2="1040"/>
    <line class="fold" x1="233" y1="262" x2="233" y2="1040"/>
    <line class="fold" x1="278" y1="262" x2="278" y2="1040"/>
    <line class="fold" x1="392" y1="262" x2="392" y2="1040"/>
    <line class="fold" x1="118" y1="262" x2="445" y2="262"/>
    <line class="fold" x1="118" y1="1040" x2="445" y2="1040"/>
    <line class="fold" x1="110" y1="160" x2="237" y2="160"/>
    <line class="fold" x1="110" y1="205" x2="237" y2="205"/>
    <line class="fold" x1="278" y1="215" x2="392" y2="215"/>

    <!-- front display window -->
    <path class="window" d="M313 830 L313 412 L298 412 Q294 412 294 416 L294 444 Q294 448 298 448 L313 448 L313 448 M313 830 L357 830 L357 448 L372 448 Q376 448 376 444 L376 416 Q376 412 372 412 L357 412 L357 328 Q357 306 335 306 Q313 306 313 328 L313 412"/>

    <!-- brand names -->
    <text class="brand-name" font-size="46" transform="translate(178 560) rotate(-90)">CordaVex</text>
    <text class="brand-name" font-size="29" transform="translate(338 935) rotate(-90)">CordaVex</text>

    <!-- back info label with UPC space -->
    <rect class="info-label" x="118" y="852" width="114" height="186"/>
    <circle class="info-bullet" cx="127" cy="864" r="1.6"/>
    <text class="info-text" x="140" y="866">
      <tspan x="140">Our tassels are made from</tspan>
      <tspan x="140" dy="7.5">the highest quality of</tspan>
      <tspan x="140" dy="7.5">polyester available.</tspan>
    </text>
    <circle class="info-bullet" cx="127" cy="894" r="1.6"/>
    <text class="info-text" x="140" y="896">
      <tspan x="140">Resulting in accurate and</tspan>
      <tspan x="140" dy="7.5">consistent school colors.</tspan>
    </text>
    <circle class="info-bullet" cx="127" cy="916" r="1.6"/>
    <text class="info-text" x="140" y="918">
      <tspan x="140">Each tassel has 50-60</tspan>
      <tspan x="140" dy="7.5">braided yarns. The signets</tspan>
      <tspan x="140" dy="7.5">are made from Zinc alloy</tspan>
      <tspan x="140" dy="7.5">or solid brass (depending</tspan>
      <tspan x="140" dy="7.5">on color).</tspan>
    </text>
    <text class="upc-note" x="176" y="993">UPC</text>
    <text class="upc-note" x="176" y="1015">CODE</text>
  </svg>
</main>
</body>
</html>
```